Commercial Landscaping Flyer Needed

Looking for a flyer design to showcase what we offer for commercial landscape Installations. We want this to illustrate what sets us apart from our competitors. Include our EMR Safety rating of .72, that our average commercial landscape installation size is $215,000 with our largest completed in 2020 being $1,375,590. We have backgrounds in commercial design and installation and help our customers with Value Engineering Strategies. Since incorporating in 2005, we have an average employment retention length of 8 years. We want this flyer to show our commercial clients that we mean business and are dedicated to making their project happen on time, run efficiently, and we do excellent work.

Need extra days to review

```html
<!DOCTYPE html>
<html lang="en">
<head>
<meta charset="utf-8">
<title>Meadowline Grounds – Commercial Landscape Installations</title>
<link rel="stylesheet" href="https://fonts.googleapis.com/css2?family=Montserrat:wght@800&family=Open+Sans:wght@600;700;800&display=swap">
<style>
  :root {
    --backdrop: #10214d;
    --paper: #ffffff;
    --lime: #b8cf1c;
    --olive: #859710;
    --olive-deep: #5f6d08;
    --charcoal: #3b3b3b;
    --ink: #2f2f2f;
    --white: #ffffff;
  }
  * { box-sizing: border-box; margin: 0; padding: 0; }
  html, body { width: 1200px; height: 1000px; overflow: hidden; }
  body { background: var(--backdrop); font-family: "Open Sans", Arial, sans-serif; }

  .flyer {
    position: absolute; left: 287px; top: 45px;
    width: 629px; height: 887px;
    background: var(--paper); overflow: hidden;
  }
  .flyer > * { position: absolute; }

  .brand { left: 0; width: 100%; top: 24px; display: flex; justify-content: center; align-items: center; gap: 8px; }
  .brand-dot { width: 22px; height: 22px; border-radius: 50%; background: var(--lime); }
  .brand-name { font-family: "Open Sans", Arial, sans-serif; font-weight: 800; font-size: 22px; color: var(--charcoal); }

  .headline { left: 0; width: 100%; text-align: center; font-family: "Montserrat", Arial, sans-serif; font-weight: 800; line-height: 1; }
  .headline-top { top: 98px; font-size: 34px; color: var(--olive); }
  .headline-bottom { top: 142px; font-size: 34px; color: var(--charcoal); }

  .band-top { left: 0; top: 175px; width: 629px; height: 32px; }
  .hero-photo {
    left: 0; top: 205px; width: 629px; height: 247px;
    background: linear-gradient(120deg, #c9b53a 0%, #6f8a3a 25%, #9d9a88 55%, #b48a6d 70%, #4f6a34 100%);
  }
  .band-bottom { left: 0; top: 440px; width: 629px; height: 40px; }

  .stat {
    top: 370px; height: 165px;
    background: linear-gradient(#879a12, #5d6a07);
    border: 2px solid rgba(255,255,255,.8);
    border-radius: 20px; color: var(--white); text-align: center;
    box-shadow: 0 14px 14px -8px rgba(0,0,0,.45);
  }
  .stat-safety { left: 40px; width: 267px; }
  .stat-size { left: 322px; width: 268px; }
  .stat-label { font-weight: 800; font-size: 26px; line-height: 31px; margin-top: 8px; }
  .stat-value-big { font-weight: 800; font-size: 86px; line-height: 86px; }
  .stat-note { font-weight: 700; font-size: 13.5px; line-height: 17px; }
  .stat-size .stat-note:first-child { margin-top: 12px; }
  .stat-value { font-weight: 800; font-size: 34px; line-height: 40px; }

  .intro { top: 548px; left: 0; width: 100%; text-align: center; font-weight: 700; font-size: 12.6px; line-height: 17px; color: var(--ink); }

  .services-panel { left: 0; top: 625px; width: 629px; height: 136px; background: var(--charcoal); }
  .services-title {
    left: 216px; top: 611px; width: 197px; height: 32px;
    background: var(--olive); border-radius: 16px;
    color: var(--white); font-weight: 800; font-size: 22px; line-height: 32px; text-align: center;
  }
  .service-column { top: 655px; list-style: none; }
  .service-column li { display: flex; align-items: flex-start; gap: 8px; color: var(--white); font-weight: 700; font-size: 16px; line-height: 19px; margin-bottom: 14px; }
  .service-column li svg { flex: none; width: 22px; height: 22px; margin-top: -2px; }
  .col-1 { left: 36px; }
  .col-2 { left: 200px; }
  .col-3 { left: 446px; }
  .col-2 li:last-child { margin-bottom: 0; }
  .divider { top: 653px; width: 2px; height: 76px; background: var(--lime); }
  .divider-1 { left: 185px; }
  .divider-2 { left: 431px; }

  .gallery-photo { top: 740px; height: 72px; border: 2px solid var(--white); }
  .photo-lawn { left: 36px; width: 134px; background: linear-gradient(#4d8a2a, #2f6a1c); }
  .photo-house { left: 177px; width: 133px; background: linear-gradient(#b9cde0, #9a8a6a 55%, #4f7a32); }
  .photo-entry { left: 317px; width: 134px; background: linear-gradient(#dbe4d4, #6a8a4a 50%, #a08a6a); }
  .photo-stone { left: 458px; width: 133px; background: linear-gradient(#3f5a2a, #a89478 60%, #c4b8a0); }

  .contact-band { left: 0; top: 832px; width: 629px; height: 55px; background: var(--olive); }
  .contact-title {
    left: 248px; top: 821px; width: 133px; height: 24px;
    background: var(--ink); border-radius: 12px;
    color: var(--white); font-weight: 800; font-size: 14px; line-height: 24px; text-align: center;
  }
  .contact-list { left: 0; top: 852px; width: 100%; display: flex; justify-content: center; align-items: center; list-style: none; }
  .contact-list li { display: flex; align-items: center; gap: 6px; color: var(--white); font-weight: 700; font-size: 19px; padding: 0 10px; }
  .contact-list li + li { border-left: 2px solid var(--olive-deep); }
  .contact-list svg { width: 20px; height: 20px; }
</style>
</head>
<body>
<main class="flyer">
  <div class="brand">
    <span class="brand-dot"></span>
    <span class="brand-name">Meadowline Grounds</span>
  </div>

  <h1 class="headline headline-top">WE OFFER COMMERCIAL</h1>
  <h2 class="headline headline-bottom">LANDSCAPE INSTALLATIONS</h2>

  <svg class="band-top" viewBox="0 0 629 32" preserveAspectRatio="none" aria-hidden="true">
    <polygon points="0,2 629,28 629,32 0,32" fill="var(--lime)"/>
  </svg>
  <div class="hero-photo" role="img" aria-label="Aerial view of a commercial courtyard with turf, planters, paved patio and seating beside a yellow building"></div>
  <svg class="band-bottom" viewBox="0 0 629 40" preserveAspectRatio="none" aria-hidden="true">
    <polygon points="300,40 629,8 629,40" fill="var(--lime)"/>
  </svg>

  <div class="stat stat-safety">
    <p class="stat-label">EMR SAFETY<br>RATING OF</p>
    <p class="stat-value-big">.72</p>
  </div>
  <div class="stat stat-size">
    <p class="stat-note">Our average commercial<br>landscape installation size is</p>
    <p class="stat-value">$215,000</p>
    <p class="stat-note">with our largest completed<br>in 2020 being</p>
    <p class="stat-value">$1,375,590</p>
  </div>

  <p class="intro">We have backgrounds in commercial design and installation<br>and help our customers with Value Engineering Strategies. Since incorporating in 2005,<br>we have an average employment retention length of 8 years.</p>

  <div class="services-panel"></div>
  <h3 class="services-title">SERVICES</h3>

  <ul class="service-column col-1">
    <li><svg viewBox="0 0 22 22"><circle cx="11" cy="11" r="9" fill="none" stroke="var(--lime)" stroke-width="2"/><path d="M6 11l4 4 9-10" fill="none" stroke="var(--lime)" stroke-width="2.4"/></svg>Hardscaping</li>
    <li><svg viewBox="0 0 22 22"><circle cx="11" cy="11" r="9" fill="none" stroke="var(--lime)" stroke-width="2"/><path d="M6 11l4 4 9-10" fill="none" stroke="var(--lime)" stroke-width="2.4"/></svg>Irrigation</li>
  </ul>
  <span class="divider divider-1"></span>
  <ul class="service-column col-2">
    <li><svg viewBox="0 0 22 22"><circle cx="11" cy="11" r="9" fill="none" stroke="var(--lime)" stroke-width="2"/><path d="M6 11l4 4 9-10" fill="none" stroke="var(--lime)" stroke-width="2.4"/></svg>Turf Management</li>
    <li><svg viewBox="0 0 22 22"><circle cx="11" cy="11" r="9" fill="none" stroke="var(--lime)" stroke-width="2"/><path d="M6 11l4 4 9-10" fill="none" stroke="var(--lime)" stroke-width="2.4"/></svg>Chemical Applications<br>&amp; Fertilization</li>
  </ul>
  <span class="divider divider-2"></span>
  <ul class="service-column col-3">
    <li><svg viewBox="0 0 22 22"><circle cx="11" cy="11" r="9" fill="none" stroke="var(--lime)" stroke-width="2"/><path d="M6 11l4 4 9-10" fill="none" stroke="var(--lime)" stroke-width="2.4"/></svg>Maintenance</li>
    <li><svg viewBox="0 0 22 22"><circle cx="11" cy="11" r="9" fill="none" stroke="var(--lime)" stroke-width="2"/><path d="M6 11l4 4 9-10" fill="none" stroke="var(--lime)" stroke-width="2.4"/></svg>Landscaping</li>
  </ul>

  <div class="gallery-photo photo-lawn" role="img" aria-label="Striped lawn with a red mower"></div>
  <div class="gallery-photo photo-house" role="img" aria-label="Stone building with landscaped front lawn"></div>
  <div class="gallery-photo photo-entry" role="img" aria-label="Entrance sign surrounded by plantings"></div>
  <div class="gallery-photo photo-stone" role="img" aria-label="Boulder garden with stone path"></div>

  <div class="contact-band"></div>
  <h3 class="contact-title">CONTACT US</h3>
  <ul class="contact-list">
    <li><svg viewBox="0 0 20 20"><circle cx="10" cy="10" r="10" fill="var(--lime)"/><path d="M7 5l2 2-1 2 3 3 2-1 2 2-2 2c-4 0-8-4-8-8z" fill="var(--olive-deep)"/></svg>555-014-2837</li>
    <li><svg viewBox="0 0 20 20"><circle cx="10" cy="10" r="10" fill="var(--lime)"/><path d="M7 5l2 2-1 2 3 3 2-1 2 2-2 2c-4 0-8-4-8-8z" fill="var(--olive-deep)"/></svg>555-019-6604</li>
    <li><svg viewBox="0 0 20 20"><circle cx="10" cy="10" r="10" fill="var(--lime)"/><circle cx="10" cy="10" r="6" fill="none" stroke="var(--olive-deep)" stroke-width="1.5"/><path d="M4 10h12M10 4c-3 3-3 9 0 12M10 4c3 3 3 9 0 12" fill="none" stroke="var(--olive-deep)" stroke-width="1.2"/></svg>meadowlinegrounds.com</li>
  </ul>
</main>
</body>
</html>
```